Business supporting small business needs: Business card, A4 letterhead, A6 postcard, C5& C6envelope

We require stationery designed for a new Australian company called "Tallow Meadow" that provides operational strategy and support to small businesses.

We already have a logo (attached).

We require:
- business card (double-sided)
- A4 letterhead (double-sided)
- A6 postcard - to be used like a with-compliments slip (double-sided)
- C5 envelope
- C6 envelope

We would like the backs of the business card, letterhead and postcard to strongly feature the blue colour from the logo.

The business card, letterhead and postcard must contain:
- Tallow Meadow
- Staff member name
- Website address
- Email address
- Phone number
- Postal address
(I will provide these details to the winner)

The letterhead must also contain the ABN: 57 382 916 204 and company name "Tallow Meadow Pty Ltd".

Our standard font is century gothic.
Updates

Thank you for the designs so far.

Please note that the only change to the logo I am open to, is using an all white logo on a blue background.

I am not open to any other changes to the logo, such as shading, shadows or other colour changes.

Target Market(s)

Small and micro business owners

Industry/Entity Type

Small Business

```html
<!DOCTYPE html>
<html lang="en">
<head>
<meta charset="utf-8">
<title>Tallow Meadow — Envelope</title>
<link rel="stylesheet" href="https://fonts.googleapis.com/css2?family=Questrial&display=swap">
<style>
  :root {
    --brand-blue: #27afcf;
    --paper: #ffffff;
    --ink-grey: #8a8a8a;
    --stage: #262626;
    --label: #9a9a9a;
    --fold-line: #8c8c8c;
  }
  html, body {
    margin: 0;
    width: 1200px;
    height: 900px;
    overflow: hidden;
    background: var(--stage);
    font-family: "Questrial", "Century Gothic", sans-serif;
  }
  .sheet-title {
    position: absolute;
    left: 37px;
    top: 32px;
    margin: 0;
    font-size: 22px;
    font-weight: normal;
    color: var(--label);
  }
  .envelope {
    position: absolute;
    top: 266px;
    width: 520px;
    height: 368px;
    background: var(--paper);
    overflow: hidden;
  }
  .envelope--front { left: 60px; }
  .envelope--back { left: 620px; }
  .envelope svg { position: absolute; inset: 0; }
  .wordmark {
    position: absolute;
    left: 36px;
    top: 44px;
    display: flex;
    align-items: center;
    gap: 8px;
    color: var(--brand-blue);
    font-size: 22px;
    line-height: 1;
  }
  .wordmark__dot {
    width: 14px;
    height: 14px;
    border-radius: 50%;
    background: var(--brand-blue);
  }
  .return-address {
    position: absolute;
    left: 41px;
    bottom: 24px;
    margin: 0;
    font-style: normal;
    font-size: 6.5px;
    line-height: 1.45;
    color: var(--ink-grey);
  }
  .side-label {
    position: absolute;
    top: 648px;
    font-size: 17px;
    color: var(--label);
  }
  .side-label--front { left: 60px; }
  .side-label--back { left: 620px; }
</style>
</head>
<body>
  <h1 class="sheet-title">Envelope</h1>

  <section class="envelope envelope--front">
    <svg width="520" height="368" viewBox="0 0 520 368">
      <defs>
        <linearGradient id="swirl-tone" x1="0" y1="1" x2="1" y2="0">
          <stop offset="0" stop-color="#27afcf"/>
          <stop offset="1" stop-color="#4cc0db"/>
        </linearGradient>
      </defs>
      <path role="img" aria-label="Large decorative swirl in brand blue sweeping up from the bottom edge"
            d="M173 368 Q320 110 520 110 L520 368 Z" fill="url(#swirl-tone)"/>
    </svg>
    <div class="wordmark"><span class="wordmark__dot"></span>Tallow Meadow</div>
    <address class="return-address">
      www.tallowmeadow.com<br>
      contact@tallowmeadow.com<br>
      T. 02 9418 6620<br>
      18 Wattle Grove Rd<br>
      Ballarat, VIC 3350<br>
      Australia
    </address>
  </section>

  <section class="envelope envelope--back">
    <svg width="520" height="368" viewBox="0 0 520 368">
      <polygon class="envelope__flap" points="0,0 520,0 496,78 24,78" fill="var(--brand-blue)"/>
      <line x1="24" y1="78" x2="2" y2="368" stroke="var(--fold-line)" stroke-width="1"/>
      <line x1="496" y1="78" x2="518" y2="368" stroke="var(--fold-line)" stroke-width="1"/>
    </svg>
  </section>

  <span class="side-label side-label--front">front</span>
  <span class="side-label side-label--back">back</span>
</body>
</html>
```